Business Card Design Project

TRX Solutions is a Electrical and Communications Services and Maintenance contractor to the Mining Oil and Gas sectors of Australia.
Our clients will be planners, Schedulers, Tradespeople and Engineers

We are yet to determine the primary colours that we will use on the business cards but the logos attached will form foundation of the colours used for logos on Business cards, Website, Uniforms, vehicles etc.

Target Market(s)

Mining engineers and shedulers

Industry/Entity Type

Contractor

Requirements
Must have
• information to be included on the card

Name: Derek Hanley
Title: Managing Director
Company: TRX Solutions Pty Ltd
Phone: 08 9XXX XXXX
Mobile 0400 318 942
email: dhanley@trxsolutionsgroup.com.au
Website www.trxsolutionsgroup.com.au

Address: U5/14 Kettering Street Kestrel Park, WA 6071
Postal Address: PO Box 7183 Kestrel Park WA 6078

Nice to have
• Double sided. Maybe the logo on the back

```html
<!DOCTYPE html>
<html lang="en">
<head>
<meta charset="utf-8">
<title>TRX Solutions – Business Card</title>
<link rel="stylesheet" href="https://fonts.googleapis.com/css2?family=Arimo:wght@400;700&display=swap">
<style>
  :root {
    --backdrop: #cbcbcb;
    --navy: #14335f;
    --navy-deep: #0a1a33;
    --navy-glow: #1b4378;
    --orange: #e0531d;
    --orange-deep: #d8431a;
    --white: #ffffff;
  }
  html, body {
    margin: 0;
    padding: 0;
    overflow: hidden;
  }
  .canvas {
    position: relative;
    width: 943px;
    height: 1200px;
    background: var(--backdrop);
    font-family: "Arimo", Arial, sans-serif;
    overflow: hidden;
  }
  .wordmark {
    display: flex;
    align-items: center;
    gap: 6px;
    color: var(--white);
    font-family: "Arimo", Arial, sans-serif;
    font-weight: 400;
    white-space: nowrap;
  }
  .wordmark__square {
    width: 0.32em;
    height: 0.32em;
    background: var(--orange);
  }
  .presentation-mark {
    position: absolute;
    top: 56px;
    right: 58px;
    font-size: 26px;
  }
  .card {
    position: absolute;
    left: 205px;
    width: 507px;
    height: 309px;
    border-radius: 18px;
    overflow: hidden;
    box-shadow: 0 6px 22px rgba(0, 0, 0, 0.18);
  }
  .card--front {
    top: 305px;
    background: radial-gradient(ellipse 70% 85% at 50% 20%, var(--navy-glow) 0%, var(--navy) 45%, var(--navy-deep) 100%);
  }
  .card--front .wordmark {
    position: absolute;
    top: 137px;
    left: 0;
    right: 0;
    justify-content: center;
    font-size: 34px;
  }
  .card__url {
    position: absolute;
    top: 268px;
    left: 0;
    right: 0;
    text-align: center;
    color: var(--white);
    font-size: 10px;
  }
  .card--back {
    top: 629px;
    background: var(--white);
  }
  .card__shapes {
    position: absolute;
    inset: 0;
    width: 100%;
    height: 100%;
  }
  .card--back .wordmark {
    position: absolute;
    top: 46px;
    left: 45px;
    font-size: 22px;
  }
  .contact {
    position: absolute;
    left: 46px;
    color: var(--white);
    font-size: 9.5px;
    line-height: 12px;
  }
  .contact--address { top: 126px; }
  .contact--lines { top: 190px; }
  .contact b { font-weight: 700; }
  .person {
    position: absolute;
    top: 122px;
    right: 79px;
    text-align: right;
    color: var(--white);
  }
  .person__name {
    font-size: 23px;
    font-weight: 700;
    letter-spacing: -0.3px;
    line-height: 24px;
  }
  .person__title {
    font-size: 9.5px;
    font-weight: 700;
  }
</style>
</head>
<body>
<div class="canvas">
  <div class="wordmark presentation-mark"><span>TRX Solutions</span><span class="wordmark__square"></span></div>

  <section class="card card--front">
    <div class="wordmark"><span>TRX Solutions</span><span class="wordmark__square"></span></div>
    <div class="card__url">www.trxsolutionsgroup.com.au</div>
  </section>

  <section class="card card--back">
    <svg class="card__shapes" viewBox="0 0 444 270" preserveAspectRatio="none" aria-hidden="true">
      <defs>
        <linearGradient id="orangeBlade" x1="0" y1="0" x2="0" y2="1">
          <stop offset="0" stop-color="var(--orange)"/>
          <stop offset="1" stop-color="var(--orange-deep)"/>
        </linearGradient>
      </defs>
      <polygon fill="var(--navy)" points="0,0 428,0 365,270 75,270 0,200"/>
      <path fill="url(#orangeBlade)" d="M428,0 L444,0 L444,125 L421,196 Q416,206 408,199 L387,175 Z"/>
    </svg>
    <div class="wordmark"><span>TRX Solutions</span><span class="wordmark__square"></span></div>
    <div class="contact contact--address">
      <b>Address:</b><br>
      U5/14 Kettering Street Kestrel Park, WA 6071<br>
      Postal Address: PO Box 7183<br>
      Kestrel Park WA 6078
    </div>
    <div class="contact contact--lines">
      <b>P</b> : 08 9XXX XXXX<br>
      <b>M</b> : 0400 318 942<br>
      <b>e</b> : dhanley@trxsolutionsgroup.com.au<br>
      <b>W</b> : www.trxsolutionsgroup.com.au
    </div>
    <div class="person">
      <div class="person__name">Derek Hanley</div>
      <div class="person__title">Managing Director</div>
    </div>
  </section>
</div>
</body>
</html>
```